Professional, Attractive, Simple Website Needed!!

We completed the design for our logo.

We need a website built out around this.

Here are a couple samples of how we want ours formatted.

http://brvntapower.com

http://www.halvorbeam.com/lp/free-quote?LeadSource=Search%20Engine&ProgramName=webquery&experience=qual&language=en&type=brd&gclid=Xq7RTPwmEYKDLAvUHbsNQkfPZrTcGwnJuoVbXeLqHmRYdAsWtPkMcNfBYgzTrUoQJhEdWvKpYaLsZbCmNDgQwTxAoKpXbT_qkR

http://morvalo.co

Reason: Extending this deadline due to our delay in providing designers with content for each page. This is coming in next 24 hours.

Reason: Due to scheduling conflicts and extended travel delays related to Puerto Rico, the deadline has been extended. Your patience is greatly appreciated.

Reason: Travel and scheduling conflicts have made it impossible to give this project the thorough review it deserves, therefore I am extending the deadline. Thank you for your patience!

Target Market(s)

Home Owners who earn 60k + household annually

Industry/Entity Type

It Professional

Coding

Coded - Design and coding required

Number of Pages Required

5+ page

Font styles to use
Serif

Colors
34a7d8
9bcb3c

Requirements
Must have
• Simple
• Lead form Entry (Ability for visitor to enter Name, number and address for a quote)
• Sleek Design
• Professional
• Testimonials
• Use color Scheme of Design Logo Attached
Nice to have
• Video when site starts
• Like this
• https://www.vidmarrow.com/watch?v=qT8mRpXw2Ka&feature=vidm.ro
Should not have
• Should not include Commercial solar
• Should not include wind power

```html
<!DOCTYPE html>
<html lang="en">
<head>
<meta charset="utf-8">
<title>Sunvale Energy — Solar That Saves</title>
<link rel="stylesheet" href="https://fonts.googleapis.com/css2?family=Montserrat:wght@400;600;700&family=Open+Sans:ital,wght@0,400;0,600;0,700;1,600&display=swap">
<style>
:root{
  --blue:#34a7d8;
  --blue-deep:#1e86c4;
  --green:#9bcb3c;
  --green-dark:#2f9a2a;
  --ink:#222;
  --muted:#555;
  --line:#d6d6d6;
  --black:#000;
  --field:#f3f3f3;
}
*{box-sizing:border-box;margin:0;padding:0}
html,body{width:1200px;height:3061px;overflow:hidden;background:#fff}
body{position:relative;font-family:"Open Sans",Arial,sans-serif;color:var(--ink)}
.abs{position:absolute}

/* Hero */
.hero{left:0;top:0;width:1200px;height:660px;background:linear-gradient(180deg,#dfeaf4 0%,#c3d6e6 22%,#7d8f99 45%,#8a98a0 60%,#5d7488 100%)}
.hero-photo{position:absolute;inset:0;background:linear-gradient(160deg,rgba(255,255,255,.55) 0%,rgba(255,255,255,0) 35%),linear-gradient(200deg,rgba(40,70,110,.0) 40%,rgba(40,80,130,.55) 100%)}
.brand{left:46px;top:40px;display:flex;align-items:center;gap:12px}
.brand-mark{width:46px;height:46px;border-radius:50%;background:var(--blue)}
.brand-name{font-family:"Montserrat",Arial,sans-serif;font-weight:700;font-size:26px;color:var(--green);line-height:1.05;width:170px}
.contact-bar{right:40px;top:34px;display:flex;align-items:center;gap:26px;font-family:"Montserrat",Arial,sans-serif;font-weight:700;font-size:18px;color:#444}
.contact-bar span{display:flex;align-items:center;gap:8px}
.social{display:flex;gap:6px}
.social i{display:block;width:28px;height:28px;border:2px solid #555;border-radius:50%}
.nav{right:40px;top:108px;display:flex;gap:40px;font-family:"Montserrat",Arial,sans-serif;font-weight:700;font-size:14px;color:var(--blue-deep)}
.nav a{color:inherit;text-decoration:none;padding-bottom:6px}
.nav a.active{color:var(--green);border-bottom:4px solid var(--green)}

.hero-box{left:182px;top:294px;width:838px;height:240px;background:rgba(30,140,200,.78);border:3px solid rgba(150,200,230,.6);border-radius:8px;text-align:center;color:#fff;padding-top:24px}
.hero-box h1{font-family:"Montserrat",Arial,sans-serif;font-weight:600;font-size:40px;letter-spacing:2px}
.hero-box p{font-family:"Montserrat",Arial,sans-serif;font-weight:600;font-size:14px;line-height:1.35;margin:10px auto 0;width:740px}

.quote-form{display:flex;gap:10px;padding:9px;background:var(--green);border-radius:6px}
.quote-form .zip{width:210px;height:40px;background:#fff;border-radius:5px;font-family:"Montserrat",Arial,sans-serif;font-weight:600;font-size:16px;color:#222;display:flex;align-items:center;justify-content:center}
.quote-form .calc{width:270px;height:40px;background:var(--black);border-radius:5px;font-family:"Montserrat",Arial,sans-serif;font-weight:700;font-size:16px;color:#fff;display:flex;align-items:center;justify-content:center}
.hero-box .quote-form{position:absolute;left:162px;top:148px}

/* Section heading */
.section-title{left:0;width:1200px;display:flex;align-items:center;justify-content:center;gap:16px;font-family:"Montserrat",Arial,sans-serif;font-weight:700;font-size:24px;color:var(--blue-deep);letter-spacing:1px}
.section-title .rule{width:70px;height:2px;background:var(--green)}
.section-title .dot{width:34px;height:34px;border-radius:50%;border:3px solid var(--blue)}

/* Reviews */
.review{top:810px;width:320px;font-size:14.5px;line-height:1.32;color:#333}
.review .qm{position:absolute;left:-36px;top:-6px;font-family:Georgia,serif;font-size:60px;line-height:1;color:#555;font-weight:700}
.review .qm-end{font-family:Georgia,serif;font-size:48px;line-height:0;color:#555;font-weight:700;vertical-align:-26px;margin-left:16px}
.avatar{width:96px;height:96px;border-radius:50%;border:4px solid var(--blue);background:linear-gradient(160deg,#e9dccf,#b99d86)}
.reviewer{left:90px;top:982px;font-weight:600;font-style:italic;font-size:17px;color:#111}

/* Promo band */
.promo{left:0;top:1066px;width:1200px;height:464px;background:linear-gradient(180deg,#57b3e3,#2a8fc9)}
.promo-photo{left:0;top:1066px;width:1200px;height:464px}
.promo-text{left:660px;top:1228px;color:#fff}
.promo-text h2{font-family:"Montserrat",Arial,sans-serif;font-weight:700;font-size:40px;letter-spacing:1px}
.promo-text h2 em{font-style:normal;color:var(--green-dark)}
.promo-text p{font-family:"Montserrat",Arial,sans-serif;font-weight:600;font-size:16px;margin-top:2px}
.btn-dark{display:flex;align-items:center;justify-content:center;background:linear-gradient(180deg,#5a5a5a,#1a1a1a);color:#fff;font-family:"Montserrat",Arial,sans-serif;font-weight:700;font-size:13px;border-radius:6px}
.promo-text .btn-dark{width:200px;height:42px;margin:20px 0 0 102px}

/* FAQ */
.faq{left:310px;width:582px}
.faq-item{height:38px;border:1px solid var(--line);border-radius:19px;display:flex;align-items:center;justify-content:space-between;padding:0 18px;font-weight:700;font-size:14px;color:#222;margin-bottom:9px;box-shadow:0 1px 2px rgba(0,0,0,.08)}
.faq-item.open{height:auto;display:block;border-radius:18px;padding:10px 18px 14px}
.faq-item.open .q{display:flex;justify-content:space-between;align-items:center}
.faq-item.open p{font-weight:400;font-size:14px;line-height:1.45;color:#333;margin-top:10px}
.chev{width:12px;height:12px}

/* Lock band */
.lock{left:0;top:2145px;width:1200px;height:137px;background:linear-gradient(90deg,#2e8fc9,#45a8dc 60%,#2f93cc)}
.lock h2{position:absolute;left:120px;top:48px;font-family:"Montserrat",Arial,sans-serif;font-weight:600;font-size:31px;color:#fff;letter-spacing:2px}
.lock .quote-form{position:absolute;left:574px;top:36px;width:508px}
.lock .zip{width:200px}
.lock .calc{width:280px}

/* Contact */
.field{height:46px;background:var(--field);border:1px solid var(--line);border-radius:4px;font-weight:600;font-size:14px;color:#333;padding:12px 16px}
.btn-send{left:500px;top:2620px;width:202px;height:40px}

/* Footer */
.footer{left:0;top:2714px;width:1200px;height:296px;background:var(--black)}
.footer .brand{left:0;width:1200px;top:50px;flex-direction:column;gap:10px}
.footer .brand-mark{width:72px;height:72px}
.footer .brand-name{width:auto;text-align:center;font-size:30px}
.footer .nav{right:auto;left:0;width:1200px;top:220px;justify-content:center;gap:48px}
.copyright{left:0;top:3010px;width:1200px;height:51px;background:#d9d9d9;font-family:"Montserrat",Arial,sans-serif;font-weight:600;font-size:11px;color:#333;text-align:center;padding-top:8px}
</style>
</head>
<body>

<!-- Hero -->
<section class="abs hero">
  <div class="hero-photo" role="img" aria-label="Aerial view of suburban rooftops fitted with solar panels under a pale sky"></div>
  <div class="abs brand"><span class="brand-mark"></span><span class="brand-name">Sunvale Energy</span></div>
  <div class="abs contact-bar">
    <span><svg width="22" height="22" viewBox="0 0 24 24"><circle cx="12" cy="12" r="11" fill="none" stroke="#555" stroke-width="2"/><path d="M8 6l2 3-1.5 1.5a8 8 0 0 0 5 5L15 14l3 2-1 2.5c-5 0-10-5-10-10z" fill="#555"/></svg>800-555-0142</span>
    <span><svg width="22" height="22" viewBox="0 0 24 24"><circle cx="12" cy="12" r="11" fill="none" stroke="#555" stroke-width="2"/><rect x="6" y="8" width="12" height="8" fill="none" stroke="#555" stroke-width="1.6"/><path d="M6 8l6 5 6-5" fill="none" stroke="#555" stroke-width="1.6"/></svg>info@sunvaleenergy.com</span>
    <span class="social"><i></i><i></i></span>
  </div>
  <nav class="abs nav"><a class="active">HOME</a><a>REVIEWS</a><a>FAQs</a><a>CONTACT</a></nav>
  <div class="abs hero-box">
    <h1>SOLAR THAT SAVES</h1>
    <p>Our solar panels not only generate energy for your home, they can also generate cash in your pocket. That's because when you go solar you can save on your monthly utility bill. The savings over time add up and allow you to plan for your future.</p>
    <div class="quote-form"><div class="zip">ENTER ZIP CODE</div><div class="calc">CALCULATE YOUR SAVINGS</div></div>
  </div>
</section>

<!-- Reviews -->
<h2 class="abs section-title" style="top:714px"><span class="rule"></span><span class="dot"></span>REVIEWS<span class="rule"></span></h2>

<div class="abs review" style="left:145px"><span class="qm">&ldquo;</span>Lorem ipsum dolor sit amet, consectetuer adipiscing elit, sed diam nonummy nibh euismod tincidunt ut laoreet dolor magna aliquam erat volu. Wisi enim ad minim veniam.<span class="qm-end">&rdquo;</span></div>
<div class="abs review" style="left:495px"><span class="qm">&ldquo;</span>Lorem ipsum dolor sit amet, consectetuer adipiscing elit, sed diam nonummy nibh euismod tincidunt ut laoreet dolor magna aliquam erat volu. Wisi enim ad minim veniam.<span class="qm-end">&rdquo;</span></div>
<div class="abs review" style="left:845px"><span class="qm">&ldquo;</span>Lorem ipsum dolor sit amet, consectetuer adipiscing elit, sed diam nonummy nibh euismod tincidunt ut laoreet dolor magna aliquam erat volu. Wisi enim ad minim veniam.<span class="qm-end">&rdquo;</span></div>

<div class="abs avatar" style="left:298px;top:918px" role="img" aria-label="Portrait photo of a reviewer"></div>
<div class="abs avatar" style="left:652px;top:918px" role="img" aria-label="Portrait photo of a reviewer"></div>
<div class="abs avatar" style="left:1000px;top:918px" role="img" aria-label="Portrait photo of a reviewer"></div>
<div class="abs reviewer">Maren Holt</div>

<!-- Promo -->
<section class="abs promo"></section>
<svg class="abs promo-photo" width="1200" height="464" viewBox="0 0 1200 464" role="img" aria-label="Brick houses with rooftop solar panels, fading into a blue-tinted row of solar homes">
  <defs><linearGradient id="housePhoto" x1="0" y1="0" x2="1" y2="1"><stop offset="0" stop-color="#9bb0c2"/><stop offset=".5" stop-color="#c9b9a0"/><stop offset="1" stop-color="#6d6459"/></linearGradient></defs>
  <polygon points="0,0 600,0 500,464 0,464" fill="url(#housePhoto)"/>
  <polygon points="600,0 1200,0 1200,464 500,464" fill="#3a9fd6" opacity=".35"/>
</svg>
<div class="abs promo-text">
  <h2>Go <em>Green</em>, Get <em>Green</em></h2>
  <p>Now you can save money while doing something for Mother Nature.</p>
  <div class="btn-dark">LEARN MORE</div>
</div>

<!-- FAQs -->
<h2 class="abs section-title" style="top:1582px"><span class="rule"></span><span class="dot"></span>FAQS<span class="rule"></span></h2>
<div class="abs faq" style="top:1658px">
  <div class="faq-item">Question 1<svg class="chev" viewBox="0 0 12 12"><path d="M2 4l4 4 4-4" fill="none" stroke="#333" stroke-width="2"/></svg></div>
  <div class="faq-item open">
    <div class="q">Question 2<svg class="chev" viewBox="0 0 12 12"><path d="M2 8l4-4 4 4" fill="none" stroke="#333" stroke-width="2"/></svg></div>
    <p>Lorem ipsum dolor sit amet, consectetuer adipiscing elit, sed diam nonummy nibh euismod tincidunt ut laoreet dolore magna aliquam erat volutpat. Ut wisi enim ad minim veniam, quis nostrud exerci tation ullamcorper suscipit lobortis nisl ut aliquip ex ea commodo consequat. Duis autem vel eum iriure dolor in hendrerit in vulputate velit esse molestie consequat, vel illum dolore eu feugiat nulla facilisis at vero eros et accumsan et iusto odio dignissim qui blandit praesent luptatum zzril delenit augue duis dolore te feugait nulla facilisi.</p>
  </div>
  <div class="faq-item">Question 3<svg class="chev" viewBox="0 0 12 12"><path d="M2 4l4 4 4-4" fill="none" stroke="#333" stroke-width="2"/></svg></div>
  <div class="faq-item">Question 4<svg class="chev" viewBox="0 0 12 12"><path d="M2 4l4 4 4-4" fill="none" stroke="#333" stroke-width="2"/></svg></div>
  <div class="faq-item">Question 5<svg class="chev" viewBox="0 0 12 12"><path d="M2 4l4 4 4-4" fill="none" stroke="#333" stroke-width="2"/></svg></div>
  <div class="faq-item">Question 6<svg class="chev" viewBox="0 0 12 12"><path d="M2 4l4 4 4-4" fill="none" stroke="#333" stroke-width="2"/></svg></div>
</div>

<!-- Lock in rate -->
<section class="abs lock" role="img" aria-label="Blue-tinted band of rooftop solar panels">
  <h2>LOCK IN YOUR RATE</h2>
  <div class="quote-form"><div class="zip">ENTER ZIP CODE</div><div class="calc">CALCULATE YOUR SAVINGS</div></div>
</section>

<!-- Contact -->
<h2 class="abs section-title" style="top:2338px"><span class="rule"></span><span class="dot"></span>CONTACT<span class="rule"></span></h2>
<div class="abs field" style="left:115px;top:2412px;width:323px">Your Name</div>
<div class="abs field" style="left:443px;top:2412px;width:322px">Your Email</div>
<div class="abs field" style="left:770px;top:2412px;width:315px">Your Subject</div>
<div class="abs field" style="left:115px;top:2472px;width:970px;height:134px">Message</div>
<div class="abs btn-dark btn-send">SEND MESSAGE</div>

<!-- Footer -->
<footer class="abs footer">
  <div class="abs brand"><span class="brand-mark"></span><span class="brand-name">Sunvale Energy</span></div>
  <nav class="abs nav"><a class="active">HOME</a><a>REVIEWS</a><a>FAQs</a><a>CONTACT</a></nav>
</footer>
<div class="abs copyright">COPYRIGHT © 2017 SUNVALE ENERGY. ALL RIGHTS RESERVED.</div>

</body>
</html>
```